Stationary for Logistics Co.
Brevin Haulage Group
Project: Stationary for Logistics Co.
Stationary for Logistics Co.  - Transportation
Creative Brief
Professional
Colin Dartley
Director of Sales
4215 Marlow Ln. Cincinnati, Ohio 45239
513.620.5174 Ext. 37
colindartley@brevinhaul.example
www.brevinhaul.example
brevinhaul brevinhaul
We need business card, letterhead and envelope design. Thanks

```html
<!DOCTYPE html>
<html lang="en">
<head>
<meta charset="utf-8">
<title>Brevin Haulage Group – Business Cards</title>
<link rel="stylesheet" href="https://fonts.googleapis.com/css2?family=Open+Sans:wght@400;600;700&display=swap">
<style>
  :root {
    --navy: #1d2f86;
    --red: #b5202e;
    --ink: #2b2b2b;
    --grey: #5f636c;
    --paper: #ffffff;
    --backdrop: #e9e7e3;
  }
  * { box-sizing: border-box; margin: 0; padding: 0; }
  html, body { width: 1200px; height: 912px; overflow: hidden; }
  body {
    background: var(--backdrop);
    font-family: "Open Sans", Arial, sans-serif;
    position: relative;
  }
  .card {
    position: absolute;
    width: 520px;
    height: 300px;
    background: var(--paper);
    border-radius: 24px;
    overflow: hidden;
    box-shadow: 0 6px 18px rgba(0,0,0,.18);
  }
  .card--front { left: 60px; top: 200px; }
  .card--back { left: 620px; top: 412px; }

  .brand { display: flex; align-items: center; gap: 10px; }
  .brand__dot { width: 44px; height: 44px; border-radius: 50%; background: var(--red); flex: none; }
  .brand__name { color: var(--navy); font-weight: 700; font-size: 25px; line-height: 1.1; white-space: nowrap; }
  .brand__tagline { color: var(--grey); font-size: 14px; letter-spacing: .9px; margin-top: 2px; white-space: nowrap; }

  .card--front .brand { position: absolute; left: 92px; top: 120px; }

  .card__band { position: absolute; inset: 0; }

  .card--back .brand { position: absolute; right: 28px; top: 30px; gap: 7px; }
  .card--back .brand__dot { width: 22px; height: 22px; }
  .card--back .brand__name { font-size: 13px; }
  .card--back .brand__tagline { font-size: 7.5px; letter-spacing: .5px; margin-top: 1px; }

  .person { position: absolute; left: 30px; top: 100px; }
  .person__name { color: var(--navy); font-weight: 600; font-size: 16px; line-height: 1.2; }
  .person__role { color: var(--ink); font-size: 12px; line-height: 1.3; }

  .contact { position: absolute; left: 30px; top: 146px; list-style: none; }
  .contact__item { display: flex; align-items: center; gap: 7px; font-size: 10.5px; color: var(--ink); line-height: 17px; white-space: nowrap; }
  .contact__icon { width: 10px; height: 10px; flex: none; fill: var(--ink); }
</style>
</head>
<body>

<section class="card card--front" aria-label="Business card front">
  <div class="brand">
    <span class="brand__dot"></span>
    <div>
      <div class="brand__name">Brevin Haulage Group</div>
      <div class="brand__tagline">Freight Management Solutions</div>
    </div>
  </div>
</section>

<section class="card card--back" aria-label="Business card back">
  <svg class="card__band" viewBox="0 0 520 300" preserveAspectRatio="none" aria-hidden="true">
    <path d="M0,258 C200,250 370,190 520,84 L520,92 C370,200 200,262 0,268 Z" fill="var(--red)"/>
    <path d="M0,273 C200,267 370,210 520,100 L520,300 L0,300 Z" fill="var(--navy)"/>
  </svg>

  <div class="brand">
    <span class="brand__dot"></span>
    <div>
      <div class="brand__name">Brevin Haulage Group</div>
      <div class="brand__tagline">Freight Management Solutions</div>
    </div>
  </div>

  <div class="person">
    <div class="person__name">Colin Dartley</div>
    <div class="person__role">Director of Sales</div>
  </div>

  <ul class="contact">
    <li class="contact__item">
      <svg class="contact__icon" viewBox="0 0 12 12"><path d="M6 0a4 4 0 0 0-4 4c0 3 4 8 4 8s4-5 4-8a4 4 0 0 0-4-4zm0 5.5A1.5 1.5 0 1 1 6 2.5a1.5 1.5 0 0 1 0 3z"/></svg>
      4215 Marlow Ln. Cincinnati, Ohio 45239
    </li>
    <li class="contact__item">
      <svg class="contact__icon" viewBox="0 0 12 12"><path d="M2.5 0.5l2 2.5-1 1.5a7 7 0 0 0 4 4l1.5-1 2.5 2-1.5 2C4.5 11 1 7.5 0.5 2z"/></svg>
      513.620.5174 Ext. 37
    </li>
    <li class="contact__item">
      <svg class="contact__icon" viewBox="0 0 12 12"><path d="M0 2h12v8H0zM1 3l5 4 5-4v-.2H1z" fill-rule="evenodd"/></svg>
      colindartley@brevinhaul.example
    </li>
    <li class="contact__item">
      <svg class="contact__icon" viewBox="0 0 12 12"><circle cx="6" cy="6" r="5.2" fill="none" stroke="var(--ink)" stroke-width="1.2"/><path d="M1 6h10M6 1c-2.5 3-2.5 7 0 10M6 1c2.5 3 2.5 7 0 10" fill="none" stroke="var(--ink)" stroke-width="1"/></svg>
      www.brevinhaul.example
    </li>
  </ul>
</section>

</body>
</html>
```